New International Co-Working Space Needs Pre-Registration Website

We need a simple but stylish pre-registration website for Corvanta, a new international Coworking space. It needs to feature four sections: a description of the space, the benefits, the offering and a pre-registration form. We are looking for a clean, modern and simple yet stylish design. The site needs to be based on the divi wordpress theme. I have attached a more thorough briefing as well as our logo and some pictures we want to use.

```html
<!DOCTYPE html>
<html lang="en">
<head>
<meta charset="utf-8">
<title>Corvanta – Pre-register now</title>
<link rel="stylesheet" href="https://fonts.googleapis.com/css2?family=Poppins:wght@400;500;600&family=Open+Sans:wght@400;600;800&display=swap">
<style>
:root{
  --honey:#f4b81f;
  --honey-text:#f3b61e;
  --ink:#222222;
  --panel:#2b2b2b;
  --footer:#232323;
  --grey:#666666;
  --light:#ffffff;
  --line:#d6d6d6;
}
*{box-sizing:border-box;margin:0;padding:0}
html,body{width:1200px;height:3046px;overflow:hidden;background:var(--light)}
body{font-family:"Open Sans",Arial,sans-serif;color:var(--ink);position:relative}
.heading{font-family:"Poppins",Arial,sans-serif;font-weight:400;font-size:52px;line-height:1;color:var(--honey-text);text-align:center}

/* header */
.site-header{position:relative;height:115px}
.brand{position:absolute;left:132px;top:32px;display:flex;align-items:center;gap:14px}
.brand-dot{width:46px;height:46px;border-radius:50%;background:var(--ink)}
.brand-name{font-family:"Poppins",Arial,sans-serif;font-weight:600;font-size:44px;color:var(--ink);line-height:1}
.util{position:absolute;top:24px;right:132px;display:flex;gap:16px}
.util-btn{height:34px;border:1px solid #cfcfcf;font-size:11px;color:#555;display:flex;align-items:center;gap:7px;padding:0 14px}
.util-btn svg{width:12px;height:12px}
.main-nav{position:absolute;right:132px;top:76px;display:flex;gap:32px;font-size:13px}
.main-nav a{color:var(--ink);text-decoration:none}
.main-nav a.active{color:var(--honey-text)}

/* hero */
.hero{position:relative;height:499px;background:linear-gradient(100deg,#cfd2d3 0%,#e7e6e2 35%,#c9ccd0 60%,#aeb4bc 100%)}
.hero-arrow{position:absolute;top:349px;width:30px;height:30px;border-radius:50%;background:rgba(0,0,0,.35);display:flex;align-items:center;justify-content:center}
.hero-arrow svg{width:12px;height:12px}
.hero-arrow.prev{left:30px}
.hero-arrow.next{right:30px}

/* space */
.space{height:346px;padding-top:92px}
.space p{width:930px;margin:36px auto 0;text-align:center;font-size:14.5px;line-height:23px;color:var(--grey)}

/* feature grid */
.feature-grid{display:grid;grid-template-columns:600px 600px;grid-template-rows:480px 480px}
.map{background:linear-gradient(135deg,#e8e8e6,#d4dccb 50%,#e5e5e3)}
.office{background:linear-gradient(180deg,#e9e9e6 0%,#cfcac2 55%,#9b7a59 100%)}
.supplies{background:linear-gradient(135deg,#d9cfc2,#b88c62 60%,#8a6a4e)}
.goodies{background:var(--panel);color:var(--light);padding:60px 120px 0 40px}
.goodies .heading{text-align:left;font-size:50px}
.goodies p{margin-top:32px;font-size:14.5px;line-height:23px}
.goodies ul{list-style:none;margin-top:24px}
.goodies li{font-size:15px;line-height:32px;display:flex;align-items:center;gap:16px}
.goodies li svg{width:9px;height:11px;flex:none}

/* offering */
.offering{height:577px;padding-top:90px}
.offer-cards{display:flex;gap:21px;margin:50px 0 0 132px}
.offer-card{position:relative;width:298px;height:297px;padding:0 20px}
.offer-card.desk{background:linear-gradient(160deg,#3a2a22,#7a2b22 70%,#2c1b15)}
.offer-card.pastry{background:linear-gradient(160deg,#5a4c3e,#8e5e2e 55%,#2f2620)}
.offer-card.table{background:linear-gradient(160deg,#56463f,#8a4a3e 60%,#3a2e2a)}
.offer-title{position:absolute;left:22px;top:190px;font-weight:800;font-size:24px;color:var(--honey-text);text-transform:uppercase;line-height:1}
.offer-sub{position:absolute;left:24px;top:222px;font-size:11px;color:var(--light)}
.offer-btn{position:absolute;left:24px;top:246px;height:30px;padding:0 16px;background:var(--honey);color:var(--ink);font-size:11.5px;display:flex;align-items:center}

/* register */
.register{height:436px;background:var(--honey);padding-top:92px}
.register .heading{color:var(--ink);font-size:54px}
.form{width:936px;margin:38px auto 0}
.row{display:flex;gap:21px}
.field{flex:1;height:41px;background:var(--light);font-size:11.5px;color:#888;padding:0 16px;display:flex;align-items:center}
.field.message{margin-top:23px}
.submit{display:block;margin:23px auto 0;width:80px;height:40px;background:var(--ink);color:var(--light);font-size:11.5px;display:flex;align-items:center;justify-content:center}

/* footer */
.site-footer{position:relative;height:113px;background:var(--footer);color:#9a9a9a;font-size:11px}
.footer-links{position:absolute;left:132px;top:34px}
.footer-links span{margin:0 8px}
.copyright{position:absolute;left:132px;top:63px}
.social{position:absolute;right:148px;top:40px;display:flex;gap:13px}
.social span{width:32px;height:32px;border-radius:50%;background:#5a5a5a}
</style>
</head>
<body>

<header class="site-header">
  <div class="brand"><span class="brand-dot"></span><span class="brand-name">Corvanta</span></div>
  <div class="util">
    <div class="util-btn"><svg viewBox="0 0 12 12"><rect x="1" y="2.5" width="10" height="7" fill="#555"/><path d="M1 3l5 3.5L11 3" stroke="#fff" fill="none"/></svg>Contact</div>
    <div class="util-btn"><svg viewBox="0 0 12 12"><circle cx="6" cy="6" r="5" fill="#555"/></svg>English<svg viewBox="0 0 12 12" style="margin-left:14px"><path d="M2 4h8L6 8z" fill="#555"/></svg></div>
  </div>
  <nav class="main-nav">
    <a class="active" href="#space">The beautiful space</a>
    <a href="#goodies">All the goodies</a>
    <a href="#offering">The offering</a>
    <a href="#register">Pre-register now!</a>
  </nav>
</header>

<section class="hero" role="img" aria-label="Photo of a smiling woman with a headset working on a laptop in a bright co-working office">
  <span class="hero-arrow prev"><svg viewBox="0 0 12 12"><path d="M8 1L3 6l5 5" stroke="#fff" stroke-width="2" fill="none"/></svg></span>
  <span class="hero-arrow next"><svg viewBox="0 0 12 12"><path d="M4 1l5 5-5 5" stroke="#fff" stroke-width="2" fill="none"/></svg></span>
</section>

<section class="space" id="space">
  <h2 class="heading">The beautiful space</h2>
  <p>Fusce nec leo ac urna pulvinar auctor. Mauris bibendum fringilla velit. Nulla in lorem at massa pellentesque posuere. Nulla tristique posuere molestie. Aliquam erat volutpat. Etiam quis aliquet risus. Duis ornare erat eget magna dapibus, in accumsan quam pharetra. Nam tempus, quam in bibendum vulputate, sapien dolor viverra nisl, vitae euismod elit turpis et nulla. Aliquam erat volutpat. Pellentesque blandit lacus eget nunc faucibus, et tincidunt eros viverra. Phasellus consequat sagittis nisi suscipit feugiat.</p>
</section>

<section class="feature-grid" id="goodies">
  <div class="map" role="img" aria-label="City map with several location pins marking the co-working spaces"></div>
  <div class="office" role="img" aria-label="Photo of a bright open office with long desks, pendant lamps and large windows"></div>
  <div class="supplies" role="img" aria-label="Photo of branded office supplies laid out on a wooden desk"></div>
  <div class="goodies">
    <h2 class="heading">All the goodies</h2>
    <p>Praesent iaculis faucibus urna sit amet lacinia. Maecenas consequat justo enim, ac mattis massa imperdiet quis. Fusce eget neque elit. Sed augue orci, elementum in magna congue.</p>
    <ul>
      <li><svg viewBox="0 0 9 11"><path d="M1.5 1l5 4.5-5 4.5" stroke="#fff" stroke-width="2" fill="none"/></svg>Vestibulum condimentum, risus ut posuere cursus</li>
      <li><svg viewBox="0 0 9 11"><path d="M1.5 1l5 4.5-5 4.5" stroke="#fff" stroke-width="2" fill="none"/></svg>Pellentesque a imperdiet dolor, et auctor</li>
      <li><svg viewBox="0 0 9 11"><path d="M1.5 1l5 4.5-5 4.5" stroke="#fff" stroke-width="2" fill="none"/></svg>Proin placerat dapibus gravida</li>
      <li><svg viewBox="0 0 9 11"><path d="M1.5 1l5 4.5-5 4.5" stroke="#fff" stroke-width="2" fill="none"/></svg>Maecenas vel tortor accumsan quam varius</li>
      <li><svg viewBox="0 0 9 11"><path d="M1.5 1l5 4.5-5 4.5" stroke="#fff" stroke-width="2" fill="none"/></svg>Aenean facilisis tincidunt lectus, id dictum</li>
      <li><svg viewBox="0 0 9 11"><path d="M1.5 1l5 4.5-5 4.5" stroke="#fff" stroke-width="2" fill="none"/></svg>Vivamus efficitur ex condimentum</li>
    </ul>
  </div>
</section>

<section class="offering" id="offering">
  <h2 class="heading">The offering</h2>
  <div class="offer-cards">
    <div class="offer-card desk" role="img" aria-label="Photo of hands writing in a notebook at a desk">
      <div class="offer-title">Donec vestibulum</div>
      <div class="offer-sub">Donec molestie nisi et tellus hendrerit vehicula</div>
      <div class="offer-btn">Pre-Register Now</div>
    </div>
    <div class="offer-card pastry" role="img" aria-label="Photo of a glazed pastry on a plate">
      <div class="offer-title">Nullam accumsan</div>
      <div class="offer-sub">Donec molestie nisi et tellus hendrerit vehicula</div>
      <div class="offer-btn">Read more</div>
    </div>
    <div class="offer-card table" role="img" aria-label="Photo of a meeting table with drinks, glasses and notes">
      <div class="offer-title">Donec sit - 30%</div>
      <div class="offer-sub">Donec molestie nisi et tellus hendrerit vehicula</div>
      <div class="offer-btn">Get Discount</div>
    </div>
  </div>
</section>

<section class="register" id="register">
  <h2 class="heading">Pre-register now!</h2>
  <div class="form">
    <div class="row">
      <div class="field">Name</div>
      <div class="field">Email</div>
      <div class="field">Phone</div>
      <div class="field">Address</div>
    </div>
    <div class="field message">Message</div>
    <div class="submit">SUBMIT</div>
  </div>
</section>

<footer class="site-footer">
  <div class="footer-links">The beautiful space<span>|</span>All the goodies<span>|</span>The offering<span>|</span>Pre-register now!</div>
  <div class="copyright">Copyright © 2017 Corvanta AG Zurich. All rights reserved.</div>
  <div class="social"><span></span><span></span><span></span><span></span></div>
</footer>

</body>
</html>
```